Business Card Designs

Looking to design a 3.5" x 2" standard business card for our employees.
The design needs to be sleek, simple, and modern. We would like our logo (attached) to be incorporated, but not in that colour, rather an outline of the logo in either gold or silver (whichever looks better).

Modern and Simple is what we are looking for, but be creative in incorporating the logo.

```html
<!DOCTYPE html>
<html lang="en">
<head>
<meta charset="utf-8">
<title>Harbourline Suites Residences – Business Card</title>
<link href="https://fonts.googleapis.com/css2?family=Open+Sans:wght@400;600;700&family=Roboto:wght@400;500&display=swap" rel="stylesheet">
<style>
  :root {
    --backdrop: #d9d8d4;
    --gold: #d1a254;
    --gold-deep: #a97a2e;
    --gold-soft: #e2bd7a;
    --paper: #ffffff;
    --ink: #555555;
    --shadow: rgba(0, 0, 0, 0.18);
  }
  * { box-sizing: border-box; margin: 0; padding: 0; }
  html, body {
    width: 1200px; height: 801px; overflow: hidden;
    background: var(--backdrop);
  }
  .stage {
    position: relative; width: 1200px; height: 801px;
    display: flex; align-items: center; justify-content: center; gap: 50px;
  }
  .card {
    position: relative; width: 525px; height: 300px;
    box-shadow: 0 10px 28px var(--shadow);
    overflow: hidden;
  }

  /* Back: contact side */
  .card--back {
    background: var(--paper);
    border: 3px solid var(--gold);
    display: flex; align-items: center;
  }
  .brand-block {
    width: 50%; height: 100%;
    display: flex; flex-direction: column; align-items: center; justify-content: center; gap: 14px;
  }
  .brand-block__mark {
    width: 26px; height: 26px; background: var(--gold);
  }
  .brand-block__name {
    font-family: "Roboto", sans-serif; font-weight: 500;
    color: var(--gold); font-size: 15px; letter-spacing: 3px;
    text-transform: uppercase; text-align: center; line-height: 1.5;
  }
  .divider {
    width: 1px; height: 190px; background: var(--gold);
  }
  .contact {
    width: 50%; padding-left: 28px;
    font-family: "Open Sans", sans-serif; color: var(--ink);
  }
  .contact__name {
    font-weight: 700; color: var(--gold); font-size: 17px; letter-spacing: 0.5px;
    text-transform: uppercase;
  }
  .contact__role { font-size: 12px; margin-bottom: 16px; }
  .contact__address { font-size: 12px; line-height: 1.5; margin-bottom: 14px; font-style: normal; }
  .contact__list { list-style: none; font-size: 11.5px; line-height: 1.75; }
  .contact__list li { display: flex; align-items: center; gap: 7px; }
  .contact__list svg { width: 10px; height: 10px; fill: var(--gold); flex: none; }

  /* Front: brand side */
  .card--front { background: var(--gold); }
  .front-mark {
    position: absolute; left: 40px; top: 40px; width: 150px; height: 220px;
    background: linear-gradient(160deg, var(--gold-deep), var(--gold-soft));
  }
  .front-name {
    position: absolute; right: 40px; bottom: 62px; text-align: right;
    font-family: "Roboto", sans-serif; color: var(--paper);
  }
  .front-name__primary { font-weight: 500; font-size: 25px; letter-spacing: 5px; text-transform: uppercase; }
  .front-name__secondary { font-weight: 400; font-size: 22px; letter-spacing: 6px; text-transform: uppercase; }
</style>
</head>
<body>
<main class="stage">
  <section class="card card--back" aria-label="Card back with contact details">
    <div class="brand-block">
      <span class="brand-block__mark"></span>
      <p class="brand-block__name">Harbourline Suites<br>Residences</p>
    </div>
    <span class="divider"></span>
    <div class="contact">
      <h1 class="contact__name">Dana Whitfield</h1>
      <p class="contact__role">President</p>
      <address class="contact__address">1180 Lakeview Crescent<br>Riverton ON M4K 2B7</address>
      <ul class="contact__list">
        <li><svg viewBox="0 0 10 10"><path d="M2 0.5 L3.6 2.6 L2.8 3.6 Q4 6 6.4 7.2 L7.4 6.4 L9.5 8 L8.3 9.5 Q4 9 0.5 1.7 Z"/></svg>555-014-2278</li>
        <li><svg viewBox="0 0 10 10"><path d="M0 2 H10 V8 H0 Z M0.6 2.3 L5 5.6 L9.4 2.3" stroke="#fff" stroke-width="0.8"/></svg>hello@harbourlinesuites.com</li>
        <li><svg viewBox="0 0 10 10"><circle cx="5" cy="5" r="4.6"/><path d="M0.6 5 H9.4 M5 0.5 V9.5 M5 0.5 Q2 5 5 9.5 M5 0.5 Q8 5 5 9.5" stroke="#fff" stroke-width="0.6" fill="none"/></svg>www.harbourlinesuites.com</li>
      </ul>
    </div>
  </section>

  <section class="card card--front" aria-label="Card front with company name">
    <div class="front-mark"></div>
    <div class="front-name">
      <p class="front-name__primary">Harbourline Suites</p>
      <p class="front-name__secondary">Residences</p>
    </div>
  </section>
</main>
</body>
</html>
```